Need a flyer to leave behind when visiting clients or at shows

Glossy colorful tri-fold flyer with the same information that is on my web site www.brevalinkpro.com. I am open to a little modern or creative take on the typical brochure. I created the web site so I can provide any raw files needed from it. I would also like the ability to edit this flyer in the future in Adobe Photoshop Elements

```html
<!DOCTYPE html>
<html lang="en">
<head>
<meta charset="utf-8">
<title>BrevaLink Pro – Tri-fold Cover</title>
<link href="https://fonts.googleapis.com/css2?family=Montserrat:wght@400;500;800;900&display=swap" rel="stylesheet">
<style>
  :root {
    --page-bg: #eeeeef;
    --purple-deep: #4b2f86;
    --purple-mid: #6a3fae;
    --purple-bright: #8a5cd0;
    --headline-dark: #3a2266;
    --headline-accent: #8558cf;
    --body-text: #2d2d35;
    --panel-light: #f1f1f3;
    --white: #ffffff;
  }
  * { margin: 0; padding: 0; box-sizing: border-box; }
  html, body {
    width: 1200px; height: 897px; overflow: hidden;
    background: var(--page-bg);
    font-family: "Montserrat", Arial, sans-serif;
  }
  .cover-panel {
    position: absolute;
    left: 405px; top: 20px;
    width: 390px; height: 857px;
    background: var(--panel-light);
    overflow: hidden;
    box-shadow: 0 10px 30px rgba(0,0,0,0.12);
  }
  .top-wave { position: absolute; left: 0; top: 0; width: 390px; height: 110px; display: block; }
  .headline-block {
    position: absolute; left: 0; top: 108px; width: 100%;
    text-align: center; padding: 0 18px;
  }
  .headline-lead {
    font-weight: 900; font-size: 17px; letter-spacing: -0.5px;
    color: var(--headline-dark);
  }
  .headline-main {
    font-weight: 900; font-size: 38px; line-height: 0.98; letter-spacing: -1px;
    color: var(--headline-accent); margin-top: 4px;
  }
  .headline-sub {
    font-weight: 500; font-size: 15.5px; line-height: 1.15;
    color: var(--body-text); margin-top: 10px;
  }
  .team-photo {
    position: absolute; left: 0; top: 290px; width: 100%; height: 330px;
    background:
      linear-gradient(180deg, rgba(241,241,243,1) 0%, rgba(241,241,243,0) 18%),
      radial-gradient(ellipse at 70% 40%, #c9c3d8 0%, #8e86aa 45%, #3e3766 100%);
  }
  .brand-band {
    position: absolute; left: 0; top: 610px; width: 100%; height: 247px;
    background: linear-gradient(160deg, var(--purple-mid) 0%, var(--purple-deep) 100%);
    display: flex; align-items: center; justify-content: center;
  }
  .brand-name {
    display: flex; align-items: center; gap: 12px;
    color: var(--white); font-weight: 800; font-size: 32px; letter-spacing: -0.5px;
  }
  .brand-mark { width: 22px; height: 22px; background: var(--white); }
</style>
</head>
<body>
  <main class="cover-panel">
    <svg class="top-wave" viewBox="0 0 390 110" preserveAspectRatio="none" aria-hidden="true">
      <rect width="390" height="110" fill="#f1f1f3"/>
      <path d="M0 0 H390 V40 C300 52 200 70 120 84 C70 92 30 98 0 104 Z" fill="#4b2f86"/>
      <path d="M0 70 C60 52 120 48 190 60 C130 74 60 90 0 104 Z" fill="#8a5cd0"/>
    </svg>

    <header class="headline-block">
      <p class="headline-lead">Increasing The Value and Security of</p>
      <h1 class="headline-main">Your Technology Resources</h1>
      <p class="headline-sub">Providing Information Technology expertise to post-acute care providers</p>
    </header>

    <div class="team-photo" role="img" aria-label="Photo of colleagues talking around a meeting table, tinted purple"></div>

    <footer class="brand-band">
      <div class="brand-name"><span class="brand-mark"></span>BrevaLink Pro</div>
    </footer>
  </main>
</body>
</html>
```